**** Business card design for VoltaNode ****

For my ICT company VoltaNode I need I need a business card design.

We design, build and host web-applications and we have our own CMS product.

Some good examples are attached.

The information should be:
Joris Tielenburg
Managing director
E: j.tielenburg@voltanode-example.nl
M: +31(0)6 57218064
T: +31(0)40 7249305
W: www.voltanode-example.nl

Address:
Berend Vlootweg 27
5612 KT Eindhoven

Industry/Entity Type

Business

Requirements
Must have
• - Use logo (see attachments)
- Double sided
- Distinctive
Nice to have
• - Place for a statement on the back-side: "Engineered with care, delivered with drive"
- HTML code (or Wordpress)
- Dark (black or dark-gray) side
- Small simple images for telephone, e-mail en Url.
- QR code (only if not disturbing), not required, just an option

```html
<!DOCTYPE html>
<html lang="en">
<head>
<meta charset="utf-8">
<title>VoltaNode business card</title>
<link href="https://fonts.googleapis.com/css2?family=Open+Sans:wght@400&family=Exo+2:wght@200&display=swap" rel="stylesheet">
<style>
  :root {
    --stage: #f4f4f4;
    --stage-edge: #cfcfcf;
    --card-white: #f9f9f9;
    --card-black: #000000;
    --brand-blue: #1a7fd0;
    --icon-blue: #8fd0f5;
    --mark-blue: #3aa6e6;
    --text-light: #d2d2d2;
    --text-grey: #c4c4c4;
    --wordmark: #5d6a74;
  }
  * { margin: 0; padding: 0; box-sizing: border-box; }
  html, body { width: 1200px; height: 1029px; overflow: hidden; }
  body {
    background: var(--stage);
    font-family: "Open Sans", sans-serif;
    position: relative;
  }
  .sheet {
    position: absolute; left: 41px; top: 41px;
    width: 1111px; height: 951px;
    border: 1px solid var(--stage-edge);
  }
  .card {
    position: absolute; top: 0;
    width: 556px; height: 951px;
    overflow: hidden;
    background: var(--card-black);
  }
  .card--front { left: 0; }
  .card--back { left: 555px; border-left: 1px solid #555; }

  .front-top {
    position: absolute; left: 0; top: 0; width: 100%; height: 538px;
    background: var(--card-white);
  }
  .front-notch {
    position: absolute; left: 64px; top: 395px; width: 160px; height: 160px;
    border-radius: 50%; background: var(--card-white);
  }
  .brand-dot {
    position: absolute; left: 90px; top: 384px; width: 108px; height: 108px;
    border-radius: 50%; background: var(--mark-blue);
  }
  .brand-name {
    position: absolute; left: 219px; top: 410px;
    font-size: 44px; line-height: 1; color: var(--wordmark);
    letter-spacing: 1px; white-space: nowrap;
  }
  .person-name {
    position: absolute; left: 219px; top: 702px;
    font-size: 24px; color: var(--brand-blue); white-space: nowrap;
  }
  .person-role {
    position: absolute; left: 219px; top: 736px;
    font-size: 22px; color: var(--text-grey); white-space: nowrap;
  }
  .web {
    position: absolute; left: 219px; top: 858px;
    display: flex; align-items: center; gap: 8px;
    font-size: 22px; color: var(--text-grey); white-space: nowrap;
  }
  .web .accent { color: var(--brand-blue); }

  .statement {
    position: absolute; left: 172px; top: 198px;
    font-family: "Exo 2", sans-serif; font-weight: 200;
    font-size: 22px; line-height: 30px; letter-spacing: 2.5px;
    color: var(--text-light); white-space: nowrap;
  }
  .back-dot {
    position: absolute; left: 160px; top: 330px; width: 156px; height: 156px;
    border-radius: 50%; background: var(--mark-blue);
  }
  .address {
    position: absolute; left: 179px; top: 612px;
    font-size: 21px; line-height: 41px; color: var(--text-light);
    white-space: nowrap;
  }
  .contacts {
    position: absolute; left: 150px; top: 736px;
    list-style: none;
  }
  .contacts li {
    display: flex; align-items: center; gap: 9px;
    height: 46px; font-size: 20px; color: var(--text-light);
    white-space: nowrap;
  }
  .icon { width: 20px; height: 20px; flex: none; }
</style>
</head>
<body>
  <div class="sheet">
    <section class="card card--front">
      <div class="front-top"></div>
      <div class="front-notch"></div>
      <div class="brand-dot"></div>
      <div class="brand-name">VoltaNode</div>

      <div class="person-name">Joris Tielenburg</div>
      <div class="person-role">Managing director</div>

      <div class="web">
        <svg class="icon" viewBox="0 0 20 20" aria-hidden="true">
          <circle cx="10" cy="10" r="8" fill="none" stroke="var(--icon-blue)" stroke-width="2"/>
          <ellipse cx="10" cy="10" rx="3.5" ry="8" fill="none" stroke="var(--icon-blue)" stroke-width="1.5"/>
          <line x1="2" y1="10" x2="18" y2="10" stroke="var(--icon-blue)" stroke-width="1.5"/>
          <line x1="3.5" y1="6" x2="16.5" y2="6" stroke="var(--icon-blue)" stroke-width="1.2"/>
          <line x1="3.5" y1="14" x2="16.5" y2="14" stroke="var(--icon-blue)" stroke-width="1.2"/>
        </svg>
        <span>www.<span class="accent">voltanode-example</span>.nl</span>
      </div>
    </section>

    <section class="card card--back">
      <div class="statement">Engineered with care,<br>delivered with drive</div>
      <div class="back-dot"></div>

      <div class="address">Berend Vlootweg 27<br>5612 KT Eindhoven</div>

      <ul class="contacts">
        <li>
          <svg class="icon" viewBox="0 0 20 20" aria-hidden="true">
            <path d="M1 4h18v13H1z" fill="var(--icon-blue)"/>
            <path d="M1 4l9 8 9-8" fill="none" stroke="#000" stroke-width="2"/>
          </svg>
          <span>j.tielenburg@voltanode-example.nl</span>
        </li>
        <li>
          <svg class="icon" viewBox="0 0 20 20" aria-hidden="true">
            <circle cx="10" cy="10" r="9" fill="var(--icon-blue)"/>
            <path d="M7 5c-1 1-1.5 2.5 0 5s3.5 4.5 5 5c1 .3 2 0 2.5-1l-2-2-1.3 1c-1-.5-2.7-2.3-3.2-3.2l1-1.3z" fill="#000"/>
          </svg>
          <span>+31(0)6 57218064</span>
        </li>
        <li>
          <svg class="icon" viewBox="0 0 20 20" aria-hidden="true">
            <path d="M3 2h5v4H6v8h2v4H3z" fill="var(--icon-blue)"/>
            <path d="M12 2h5v16h-5v-4h2V6h-2z" fill="var(--icon-blue)"/>
          </svg>
          <span>+31(0)40 7249305</span>
        </li>
      </ul>
    </section>
  </div>
</body>
</html>
```